Harlow Grading LLC business card design

Excavation company business cards

Contact Information for Business Card

Harlow Grading LLC cell phone 208-471-9360 office phone 208-396-4815 harlowgradingllc@mailverde.net Driveways, site prep, retaining walls, septic systems, rock delivery

Colors

Designer to choose colors to be used in the design.

```html
<!DOCTYPE html>
<html lang="en">
<head>
<meta charset="utf-8">
<title>Harlow Grading LLC — Business Card</title>
<link href="https://fonts.googleapis.com/css2?family=Michroma&family=Montserrat:wght@400;500;800&display=swap" rel="stylesheet">
<style>
  :root {
    --backdrop: #c9c9c9;
    --card: #3e3e3e;
    --card-edge: #ff5a00;
    --accent: #f05a14;
    --ink-light: #e6e6e6;
    --rule: #9a9a9a;
  }
  * { box-sizing: border-box; margin: 0; padding: 0; }
  html, body {
    width: 1200px; height: 800px; overflow: hidden;
    background: var(--backdrop);
  }
  .canvas {
    width: 1200px; height: 800px;
    display: flex; align-items: center; justify-content: center; gap: 60px;
  }
  .card {
    width: 525px; height: 300px;
    background: var(--card);
    border-bottom: 3px solid var(--card-edge);
    border-right: 2px solid var(--card-edge);
    position: relative;
    box-shadow: 0 14px 30px rgba(0,0,0,0.28);
    overflow: hidden;
  }
  /* Contact side */
  .card--contact {
    display: flex; align-items: center; justify-content: center; gap: 20px;
    padding: 0 30px;
  }
  .identity { text-align: right; white-space: nowrap; }
  .identity__name {
    font-family: "Michroma", sans-serif;
    color: var(--accent);
    font-size: 14px; letter-spacing: 0.3px;
    text-transform: uppercase;
  }
  .identity__title {
    font-family: "Montserrat", sans-serif;
    color: var(--ink-light);
    font-size: 13px; margin-top: 3px;
  }
  .divider {
    width: 1px; height: 80px; background: var(--rule); flex: none;
  }
  .contact-list { list-style: none; white-space: nowrap; }
  .contact-list__item {
    display: flex; align-items: center; gap: 8px;
    font-family: "Montserrat", sans-serif;
    font-size: 12px; color: var(--ink-light);
    line-height: 19px;
  }
  .contact-list__icon { width: 11px; height: 11px; flex: none; }
  /* Brand side */
  .card--brand {
    display: flex; align-items: center; justify-content: center;
  }
  .brand { display: flex; align-items: center; gap: 12px; white-space: nowrap; }
  .brand__dot {
    width: 20px; height: 20px; border-radius: 50%; background: var(--accent); flex: none;
  }
  .brand__name {
    font-family: "Montserrat", sans-serif;
    font-weight: 800;
    color: var(--accent);
    font-size: 30px; letter-spacing: 1px;
    text-transform: uppercase;
  }
</style>
</head>
<body>
<main class="canvas">
  <section class="card card--contact" aria-label="Business card, contact side">
    <div class="identity">
      <p class="identity__name">Dana Whitcombe</p>
      <p class="identity__title">President</p>
    </div>
    <div class="divider"></div>
    <ul class="contact-list">
      <li class="contact-list__item">
        <svg class="contact-list__icon" viewBox="0 0 12 12" aria-hidden="true"><path d="M2.5 1 L4.5 1 L5 3.5 L3.8 4.4 Q5 7 7.6 8.2 L8.5 7 L11 7.5 L11 9.5 Q10.5 11 9 11 Q1 10 1 2.8 Q1 1.2 2.5 1 Z" fill="var(--accent)"/></svg>
        208-396-4815
      </li>
      <li class="contact-list__item">
        <svg class="contact-list__icon" viewBox="0 0 12 12" aria-hidden="true"><rect x="3" y="1" width="6" height="10" rx="1" fill="none" stroke="var(--accent)" stroke-width="1.3"/><circle cx="6" cy="9.2" r="0.7" fill="var(--accent)"/></svg>
        208-471-9360
      </li>
      <li class="contact-list__item">
        <svg class="contact-list__icon" viewBox="0 0 12 12" aria-hidden="true"><rect x="1" y="2.5" width="10" height="7" fill="var(--accent)"/><path d="M1 2.5 L6 6.5 L11 2.5" fill="none" stroke="var(--card)" stroke-width="1"/></svg>
        harlowgradingllc@mailverde.net
      </li>
      <li class="contact-list__item">
        <svg class="contact-list__icon" viewBox="0 0 12 12" aria-hidden="true"><circle cx="6" cy="6" r="5" fill="var(--accent)"/><path d="M1 6 H11 M6 1 Q3 6 6 11 M6 1 Q9 6 6 11" fill="none" stroke="var(--card)" stroke-width="0.8"/></svg>
        harlowgrading-works.com
      </li>
    </ul>
  </section>

  <section class="card card--brand" aria-label="Business card, brand side">
    <div class="brand">
      <span class="brand__dot"></span>
      <p class="brand__name">Harlow Grading LLC</p>
    </div>
  </section>
</main>
</body>
</html>
```